Tri-Fold Brochure Redesign for Floral Preservation Business

I would like to redesign my current tri-fold brouchue that I created myself and have it updated. I would like to keep the same content, color and images, but have it redesigned to look fresher and updated. I'm in the the floral preservation business and work with brides in the wedding inductry. I'm looking for a royal/rustic feel and it should relate to the look and feel of my website www.larkmeadowbloom.com. I have included the Photoshop file I used to create my orginal bouchure.

The only content that has changed is my address which is now;
4827 Maple Brook Lane, Reston VA 20194

Safe Zone Width - 10.875
Safe Zone Height - 8.375

I have included the Photoshop and Illustrator templates for the tri-fold brochure from the printer I will be using.

```html
<!DOCTYPE html>
<html lang="en">
<head>
<meta charset="utf-8">
<title>Lark Meadow Bloom – Tri-Fold Brochure</title>
<link rel="stylesheet" href="https://fonts.googleapis.com/css2?family=Cormorant+Garamond:wght@500;600&family=Open+Sans:wght@400;600;700&display=swap">
<style>
  :root{
    --canvas:#e4e6e8;
    --paper:#f2f2f1;
    --damask:#e5e5e3;
    --ink:#4a4a4a;
    --ink-soft:#777;
    --accent:#b3262f;
    --frame:#555b60;
    --link:#2f5fa8;
    --rose-light:#e46a80;
    --rose-deep:#8e2a3c;
    --bark:#5a3b30;
  }
  *{box-sizing:border-box;margin:0;padding:0}
  html,body{width:1200px;height:800px;overflow:hidden;background:var(--canvas)}
  body{font-family:"Open Sans",Arial,sans-serif;color:var(--ink)}

  .brochure{
    position:absolute;left:45px;top:30px;width:1110px;height:740px;
    display:flex;box-shadow:0 6px 24px rgba(0,0,0,.15);
  }
  .panel{position:relative;width:370px;height:100%;background:var(--paper);overflow:hidden}
  .panel + .panel{border-left:1px solid #d6d6d4}
  .damask{position:absolute;inset:0;background:linear-gradient(160deg,var(--paper),var(--damask))}
  .panel-content{position:relative;height:100%}

  .brand{display:flex;align-items:center;justify-content:center;gap:8px;
    font-family:"Cormorant Garamond",Georgia,serif;font-weight:600;color:var(--frame);letter-spacing:.04em}
  .brand-mark{width:14px;height:14px;background:var(--accent)}

  /* About panel */
  .about{padding:95px 40px 0}
  .about .brand{font-size:24px;margin-bottom:60px}
  .about h2{color:var(--accent);font-size:17px;font-weight:700;letter-spacing:.03em;margin-bottom:6px}
  .about p{font-size:11.5px;line-height:1.55;margin-bottom:16px;text-align:justify}
  .owner{font-size:13px;line-height:1.45;margin-top:20px}
  .signature{width:130px;height:30px;margin-top:6px;background:linear-gradient(90deg,rgba(179,38,47,.35),rgba(179,38,47,.1));border-radius:3px}

  /* shared band + badge */
  .band{position:absolute;left:0;right:0;height:44px;background:#fff;
    border-top:2px dotted var(--frame);border-bottom:2px dotted var(--frame)}
  .badge{position:absolute;left:50%;transform:translateX(-50%);background:#fff;
    border:5px solid var(--frame);border-radius:22px;display:flex;align-items:center;justify-content:center}
  .badge::after{content:"";position:absolute;inset:3px;border:1px solid var(--frame);border-radius:16px}

  /* back panel */
  .back .band{top:418px}
  .back .badge{top:394px;width:150px;height:92px}
  .back .badge .brand{font-size:15px;flex-direction:column;gap:4px}
  .contact{position:absolute;top:525px;left:0;right:0;text-align:center}
  .contact .appointments{color:var(--accent);font-weight:700;font-size:12px;margin-bottom:8px}
  .contact .details{font-size:10px;line-height:1.5;color:var(--ink-soft)}
  .social{display:flex;align-items:center;justify-content:center;gap:8px;margin-top:12px}
  .social-square{width:26px;height:26px;background:var(--link)}
  .social-text{font-size:11px;font-weight:700;color:var(--link);text-align:left;line-height:1.3}
  .social-handle{margin-top:6px;font-size:11px;font-weight:700;color:var(--link)}

  /* cover panel */
  .cover-photo{position:absolute;top:0;left:0;right:0;height:285px;
    background:radial-gradient(ellipse at 65% 40%,var(--rose-light) 0%,#c9405a 40%,var(--rose-deep) 70%,var(--bark) 100%)}
  .cover .band{top:290px}
  .cover .badge{top:248px;width:190px;height:128px}
  .cover .badge .brand{font-size:20px;flex-direction:column;gap:6px}
  .tagline{position:absolute;top:400px;left:40px;right:40px;text-align:center;
    font-family:"Cormorant Garamond",Georgia,serif;font-weight:500;font-variant:small-caps;
    font-size:16px;letter-spacing:.08em;line-height:1.35;color:var(--frame)}
</style>
</head>
<body>
<main class="brochure">
  <section class="panel about-panel">
    <div class="damask" role="img" aria-label="Soft grey damask pattern background"></div>
    <div class="panel-content about">
      <div class="brand"><span class="brand-mark"></span>Lark Meadow Bloom</div>
      <h2>ABOUT US</h2>
      <p>With a rich family history in the floral business spanning over 60 years, I have spent the past two decades learning all aspects of the business but focusing primarily on perfecting the freeze-dry floral preservation process. Most recently I have expanded beyond the conventional framed offerings and have learned the art of creating flower petal jewelry from preserved flowers. I'm proud to be one of the few companies in the U.S. to offer this unique service.</p>
      <p>At Lark Meadow Bloom we are committed to being the premiere floral preservation company in your community. I am extremely proud and honored to carry on the family name in the floral business by providing these services not only in my hometown of Washington DC but also in the Hampton Roads metro area. I'm confident the services offered by Lark Meadow Bloom are sure to exceed your expectations for years to come.</p>
      <div class="owner">Owner &amp; Operator<br>Lark Meadow Bloom</div>
      <div class="signature" role="img" aria-label="Handwritten signature of Clara Wendell"></div>
    </div>
  </section>

  <section class="panel back">
    <div class="damask" role="img" aria-label="Soft grey damask pattern background"></div>
    <div class="panel-content">
      <div class="band"></div>
      <div class="badge"><div class="brand"><span class="brand-mark"></span>Lark Meadow Bloom</div></div>
      <div class="contact">
        <div class="appointments">By Appointments only</div>
        <div class="details">4827 Maple Brook Lane, Reston VA 20194<br>703.555.0148 | www.larkmeadowbloom.com</div>
        <div class="social">
          <span class="social-square"></span>
          <div class="social-text">Become a fan and view<br>our most recent work</div>
        </div>
        <div class="social-handle">@larkmeadowbloom</div>
      </div>
    </div>
  </section>

  <section class="panel cover">
    <div class="damask" role="img" aria-label="Soft grey damask pattern background"></div>
    <div class="cover-photo" role="img" aria-label="Photograph of a bouquet of pink roses on rustic wood"></div>
    <div class="panel-content">
      <div class="band"></div>
      <div class="badge"><div class="brand"><span class="brand-mark"></span>Lark Meadow Bloom</div></div>
      <p class="tagline">The National Capital's Premier<br>Flower Preservation Professionals</p>
    </div>
  </section>
</main>
</body>
</html>
```